K&R Security Services PTY. LTD.

Ive just had my logo made and I'm looking for some simple but strong designs for my business cards the company is a security company.

Please use dark colors.

Regards,

Owen Deloit

Reason: Need more time for discussion with other directors

Industry/Entity Type

Security

Font styles to use
Sans Serif
Decorative

```html
<!DOCTYPE html>
<html lang="en">
<head>
<meta charset="utf-8">
<title>K&amp;R Security Services – Business Card</title>
<link rel="stylesheet" href="https://fonts.googleapis.com/css2?family=Open+Sans:wght@300;400;600&display=swap">
<style>
  :root {
    --backdrop: #e6e6e4;
    --card-dark: #3e4145;
    --card-dark-edge: #34373a;
    --card-light: #f4f4f3;
    --ink: #1c1c1c;
    --ink-soft: #8d8f91;
    --mark-faint: #5a5d61;
    --band-dark: #8b8d90;
    --band-light: #b9babb;
    --accent-bar: #8e9093;
  }
  * { box-sizing: border-box; margin: 0; padding: 0; }
  html, body { width: 1200px; height: 723px; overflow: hidden; }
  body {
    background: var(--backdrop);
    font-family: "Open Sans", sans-serif;
    position: relative;
  }
  .card {
    position: absolute;
    top: 38px;
    width: 369px;
    height: 646px;
    overflow: hidden;
    box-shadow: 0 10px 28px rgba(0,0,0,.22);
  }
  .card--front { left: 196px; background: linear-gradient(160deg, var(--card-dark), var(--card-dark-edge)); }
  .card--back { left: 635px; background: var(--card-light); }

  .base-band { position: absolute; left: 0; bottom: 0; width: 100%; height: 26px; }
  .card--front .base-band { background: var(--band-dark); }
  .card--back .base-band { background: var(--band-light); }

  /* Front: company name as faint decoration */
  .front-mark {
    position: absolute;
    top: 200px; left: 0; width: 100%;
    display: flex; flex-direction: column; align-items: center; gap: 22px;
  }
  .front-mark__circle { width: 40px; height: 40px; border-radius: 50%; background: var(--mark-faint); }
  .front-mark__name {
    font-weight: 400; font-size: 30px; line-height: 1.2; letter-spacing: 3px;
    text-transform: uppercase; text-align: center; color: var(--mark-faint);
  }

  /* Back */
  .back-mark {
    position: absolute; top: 60px; right: 36px;
    display: flex; align-items: center; gap: 10px;
  }
  .back-mark__circle { width: 16px; height: 16px; border-radius: 50%; background: var(--ink); }
  .back-mark__name {
    font-weight: 400; font-size: 17px; letter-spacing: 2px;
    text-transform: uppercase; color: var(--ink); line-height: 1;
  }

  .details {
    position: absolute; top: 226px; left: 38px; right: 20px;
    border-left: 5px solid var(--accent-bar);
    padding-left: 16px;
  }
  .company {
    font-size: 21px; line-height: 1.05; text-transform: uppercase;
    font-weight: 400; color: var(--ink); letter-spacing: .3px;
  }
  .company__muted { color: var(--ink-soft); font-weight: 300; }
  .person { margin-top: 26px; }
  .person__name { font-weight: 300; font-size: 31px; color: var(--ink-soft); line-height: 1.05; }
  .person__role { font-size: 15px; color: var(--ink); font-weight: 400; }
  .contact { margin-top: 22px; list-style: none; font-size: 14px; line-height: 1.28; }
  .contact li { color: var(--ink); }
  .contact li.contact--muted { color: var(--ink-soft); }
</style>
</head>
<body>

  <section class="card card--front" aria-label="Card front">
    <div class="front-mark">
      <span class="front-mark__circle"></span>
      <span class="front-mark__name">K&amp;R<br>Security<br>Services</span>
    </div>
    <div class="base-band"></div>
  </section>

  <section class="card card--back" aria-label="Card back">
    <div class="back-mark">
      <span class="back-mark__circle"></span>
      <span class="back-mark__name">K&amp;R Security</span>
    </div>

    <div class="details">
      <h1 class="company">K&amp;R<br>Security<br><span class="company__muted">Services</span></h1>
      <div class="person">
        <p class="person__name">Your Name</p>
        <p class="person__role">manager director</p>
      </div>
      <ul class="contact">
        <li>m: 0400 118 362</li>
        <li class="contact--muted">p: (03) 9000 4417</li>
        <li>e: owen@krsecurity.net.au</li>
        <li>e: info@krsecurity.net.au</li>
        <li class="contact--muted">a: P.O. Box 12 Northvale Victoria 3000</li>
      </ul>
    </div>

    <div class="base-band"></div>
  </section>

</body>
</html>
```